MOLVT Study flyer

I need help designing a flyer for a research study that will include brain imaging in adolescents. The info is in the attached document. The study is called the Marrowby Orchard Lantern Vesper Trail (MOLVT) study. Ideally this would be returned as a document that I can edit in the future as we will have several new recruitment phases (different age groups, etc. I also would love to have a logo designed as part of this project, but I recognize that might be a separate design request.

```html
<!DOCTYPE html>
<html lang="en">
<head>
<meta charset="utf-8">
<title>MOLVT Study Flyer</title>
<link rel="stylesheet" href="https://fonts.googleapis.com/css2?family=Poppins:wght@400;700&family=Source+Sans+3:ital,wght@0,400;0,600;0,700;1,700&display=swap">
<style>
  :root {
    --navy: #2b2f86;
    --magenta: #e6007e;
    --yellow: #f7ea1c;
    --orange: #f7931e;
    --lime: #b9d80f;
    --green: #7cc242;
    --paper: #e9e9ea;
    --blue-deep: #1b2f98;
    --blue-mid: #1560b8;
    --blue-light: #1a8fd3;
    --white: #ffffff;
    --ink: #1c1c1c;
    --backdrop: #ededed;
  }
  * { box-sizing: border-box; margin: 0; padding: 0; }
  html, body { width: 1064px; height: 1200px; overflow: hidden; }
  body { background: var(--backdrop); position: relative; font-family: "Source Sans 3", sans-serif; }

  .flyer {
    position: absolute; left: 106px; top: 0; width: 852px; height: 1200px;
    overflow: hidden; background: var(--paper);
  }
  .flyer-bg { position: absolute; inset: 0; }

  .photo-area {
    position: absolute; left: 14px; top: 228px; width: 366px; height: 420px;
    background: radial-gradient(ellipse at 50% 40%, #d9cfc6 0%, #e4e0dc 45%, rgba(233,233,234,0) 75%);
  }

  .headline { position: absolute; left: 66px; font-family: "Poppins", sans-serif; font-weight: 700; letter-spacing: -1.5px; line-height: 1; }
  .headline-top { top: 44px; font-size: 48px; color: var(--navy); }
  .headline-accent { top: 114px; font-size: 56px; color: var(--magenta); }

  .question {
    position: absolute; left: 388px; top: 272px; width: 440px;
    font-family: "Poppins", sans-serif; font-weight: 700; font-size: 38px;
    line-height: 50px; color: var(--navy); letter-spacing: -0.5px;
  }
  .intro {
    position: absolute; left: 388px; top: 462px; width: 400px;
    font-family: "Poppins", sans-serif; font-size: 12.5px; line-height: 21px; color: var(--ink);
  }
  .rule { position: absolute; left: 388px; top: 578px; width: 360px; height: 1px; background: #9a9a9a; }
  .compensation { position: absolute; left: 388px; top: 588px; font-weight: 700; font-size: 19px; color: var(--magenta); }

  .worry-badge {
    position: absolute; left: 86px; top: 551px; width: 220px; height: 220px; border-radius: 50%;
    background: radial-gradient(circle at 50% 20%, #f0308f 0%, var(--magenta) 55%, #d40072 100%);
    box-shadow: 0 6px 14px rgba(0,0,0,0.25);
    display: flex; flex-direction: column; align-items: center; justify-content: center;
    font-weight: 700; font-size: 27px; line-height: 30px; text-align: center;
  }
  .worry-badge .hl { color: var(--yellow); }
  .worry-badge .wh { color: var(--white); font-size: 25px; }

  .details { position: absolute; left: 51px; width: 500px; }
  .detail-title { font-weight: 600; font-size: 19px; color: var(--yellow); }
  .detail-body { font-family: "Poppins", sans-serif; font-size: 12.5px; line-height: 21.5px; color: var(--white); margin-top: 8px; }
  .details-1 { top: 806px; }
  .details-2 { top: 914px; }

  .cta { position: absolute; left: 51px; top: 1064px; }
  .cta-title { font-style: italic; font-weight: 700; font-size: 29px; color: var(--yellow); }
  .cta-sub { font-weight: 700; font-size: 15.5px; color: var(--yellow); margin-top: 0; }
  .cta-email { font-weight: 600; font-size: 23px; color: var(--white); margin-top: 22px; letter-spacing: 0.2px; }

  .eligibility-pill {
    position: absolute; left: 600px; top: 800px; width: 189px; height: 325px;
    background: var(--magenta); border-radius: 0 0 95px 95px;
    box-shadow: 0 6px 14px rgba(0,0,0,0.25);
    padding-top: 126px; text-align: center; color: var(--white);
    font-weight: 600; font-size: 23px;
  }
  .eligibility-pill span { display: block; line-height: 29px; border-bottom: 1px solid rgba(255,255,255,0.25); margin: 0 14px; }
  .eligibility-pill span:last-child { border-bottom: none; }
  .eligibility-circle {
    position: absolute; left: 585px; top: 698px; width: 220px; height: 220px; border-radius: 50%;
    background: radial-gradient(circle at 50% 35%, #ffffff 0%, #f2f2f2 60%, #d6d6d6 100%);
    box-shadow: 0 5px 12px rgba(0,0,0,0.3);
    text-align: center; padding-top: 36px;
  }
  .eligibility-lead { font-weight: 600; font-size: 18.5px; line-height: 23px; color: var(--ink); }
  .eligibility-age { font-weight: 700; font-size: 28px; line-height: 32px; color: var(--navy); margin-top: 8px; }
  .eligibility-age-num { font-weight: 700; font-size: 34px; line-height: 36px; color: var(--navy); }
</style>
</head>
<body>
<main class="flyer">
  <svg class="flyer-bg" width="852" height="1200" viewBox="0 0 852 1200" aria-hidden="true">
    <defs>
      <linearGradient id="sunBand" x1="0" y1="0" x2="1" y2="0.25">
        <stop offset="0" stop-color="#f47a1f"/>
        <stop offset="0.35" stop-color="#f8c51a"/>
        <stop offset="0.6" stop-color="#e5e414"/>
        <stop offset="1" stop-color="#7cc242"/>
      </linearGradient>
      <linearGradient id="seaBand" x1="0" y1="1" x2="1" y2="0">
        <stop offset="0" stop-color="#1b2f98"/>
        <stop offset="0.55" stop-color="#1a44a8"/>
        <stop offset="1" stop-color="#1470c4"/>
      </linearGradient>
    </defs>
    <path fill="url(#sunBand)" d="M0 0H852V262L830 258 812 270 790 252 770 262 745 250 720 262 700 246 680 258 652 244 630 262 610 250 590 268 560 252 540 264 520 250 495 258 470 240 448 250 420 236 395 246 370 232 345 240 320 226 300 236 280 222 250 232 230 222 200 236 180 224 150 240 120 228 95 244 70 238 50 256 28 250 10 266 0 262Z"/>
    <path fill="url(#seaBand)" d="M0 1200V640L18 636 38 646 60 632 82 644 104 636 130 650 160 640 190 656 230 648 270 660 310 650 340 642 370 652 400 642 430 634 460 644 490 632 520 640 550 628 580 636 610 626 640 632 670 622 700 630 730 620 760 626 790 616 820 624 852 614V1200Z"/>
    <path fill="var(--blue-light)" opacity="0.7" d="M410 1200C470 1180 520 1160 560 1130C620 1090 660 1110 720 1060C770 1020 780 980 852 946V1200Z"/>
    <path fill="#1f86cc" opacity="0.6" d="M470 1200C540 1190 590 1170 640 1140C700 1105 740 1120 790 1080C820 1055 830 1020 852 1000V1200Z"/>
  </svg>

  <div class="photo-area" role="img" aria-label="Photograph of a dark-haired teenage girl in a white top, eyes closed, hands raised in a calm meditative pose"></div>

  <h1 class="headline headline-top">Are you the parent of a</h1>
  <p class="headline headline-accent">Child Age 10–17?</p>

  <h2 class="question">Do they worry or overthink negative emotions?</h2>
  <p class="intro">Halverton University researchers are seeking girls age 10-17 for a study about brain activity in emotions and decision-making and how they relate to puberty, anxiety and depression.</p>
  <div class="rule"></div>
  <p class="compensation">Compensation up to $140</p>

  <div class="worry-badge">
    <span class="hl">Tend to</span>
    <span class="hl">worry or</span>
    <span class="wh">Overthink</span>
    <span class="wh">Negative</span>
    <span class="wh">Thoughts</span>
  </div>

  <section class="details details-1">
    <h3 class="detail-title">Study participation involves:</h3>
    <p class="detail-body">One one-hour interview (online or in-person) where<br>your child will discuss their thoughts</p>
  </section>
  <section class="details details-2">
    <h3 class="detail-title">Online questionnaires (parent and child)</h3>
    <p class="detail-body">One two-hour visit where your child will complete an MRI scan, answer questions about their puberty stage, and have a small hair sample taken to study puberty hormones</p>
  </section>

  <section class="cta">
    <h3 class="cta-title">Interested in participating?</h3>
    <p class="cta-sub">Want more information? Please contact us!</p>
    <p class="cta-email">molvtstudy@halvertonhealth.edu</p>
  </section>

  <div class="eligibility-pill">
    <span>have not been</span>
    <span>diagnosed</span>
    <span>with psychosis,</span>
    <span>learning</span>
    <span>problems, or</span>
    <span>autism</span>
  </div>
  <div class="eligibility-circle">
    <p class="eligibility-lead">Your child<br>may be eligible<br>if they:</p>
    <p class="eligibility-age">Are Age</p>
    <p class="eligibility-age-num">10-17</p>
  </div>
</main>
</body>
</html>
```